Awesome Dessert Baker needs Sticker Design

My wife is an incredible baker. She specializes in desserts and everyone that tastes her baked goods has told her to start selling them. She recently decided to go into business and just through word of mouth and her reputation she is already getting steady orders.

She is looking to have a sticker developed to put on her cake boxes and packaging.

She wants the following:
1. Colors to be used- hot pink, purple, white
2. Want a sleek, modern design and style incorporating following:
name: Whisked by Nola
tel: 917 382 6140
email: nola@whiskedbynola.example

**no old fashion baking references like rolling pins, aprons, ect.

We want the sticker to be very appealing and eye catching that will further promote her image and business.

Industry/Entity Type

Fashion

Requirements
Must have
• Must contain the following information:

Whisked by Nola
917 382 6140 (please make small and discreet)
nola@whiskedbynola.example (please make small and discreet)
Should not have
• **no old fashion baking references like rolling pins, aprons, ect.

```html
<!DOCTYPE html>
<html lang="en">
<head>
<meta charset="utf-8">
<title>Whisked by Nola — Sticker</title>
<link rel="stylesheet" href="https://fonts.googleapis.com/css2?family=Tenor+Sans&display=swap">
<style>
  :root {
    --page-bg: #f1f1f1;
    --sticker-purple: #6b1e79;
    --doily-white: #ffffff;
    --ink-plum: #3b0b45;
    --ribbon-magenta: #b43acf;
    --ribbon-glow: #dc97e3;
    --ribbon-fold: #3c0c46;
    --ribbon-text: #ffffff;
  }
  html, body {
    margin: 0;
    width: 1200px;
    height: 900px;
    overflow: hidden;
    background: var(--page-bg);
  }
  .sticker {
    display: block;
    width: 1200px;
    height: 900px;
  }
  .sticker__base { fill: var(--sticker-purple); }
  .sticker__doily { fill: var(--doily-white); }
  .brand-name {
    font-family: "Tenor Sans", "Trebuchet MS", sans-serif;
    fill: var(--ink-plum);
    text-anchor: middle;
  }
  .brand-name__lead { font-size: 50px; letter-spacing: 3px; }
  .brand-name__main { font-size: 104px; letter-spacing: 16px; }
  .ribbon__band { fill: url(#ribbonGradient); }
  .ribbon__fold { fill: var(--ribbon-fold); }
  .ribbon__text {
    font-family: "Tenor Sans", "Trebuchet MS", sans-serif;
    fill: var(--ribbon-text);
    text-anchor: middle;
  }
  .ribbon__text--phone { font-size: 28px; letter-spacing: 4px; }
  .ribbon__text--email { font-size: 25px; letter-spacing: 1.5px; }
</style>
</head>
<body>
<svg class="sticker" viewBox="0 0 1200 900" xmlns="http://www.w3.org/2000/svg">
  <defs>
    <linearGradient id="ribbonGradient" x1="0" y1="0" x2="1" y2="0">
      <stop offset="0" stop-color="var(--ribbon-magenta)"/>
      <stop offset="0.45" stop-color="var(--ribbon-glow)"/>
      <stop offset="0.8" stop-color="var(--ribbon-magenta)"/>
      <stop offset="1" stop-color="var(--ribbon-magenta)"/>
    </linearGradient>
  </defs>

  <circle class="sticker__base" cx="600" cy="442" r="350"/>
  <circle class="sticker__doily" cx="600" cy="440" r="295" role="img" aria-label="White lace paper doily with cut-out pattern"/>

  <text class="brand-name brand-name__lead" x="598" y="405">WHISKED BY</text>
  <text class="brand-name brand-name__main" x="604" y="517">NOLA</text>

  <g class="ribbon" transform="rotate(-14 640 610)">
    <polygon class="ribbon__fold" points="905,540 945,556 905,556"/>
    <polygon class="ribbon__band" points="330,556 945,556 945,612 350,612"/>
    <polygon class="ribbon__fold" points="392,612 432,612 392,628"/>
    <polygon class="ribbon__band" points="392,626 955,626 955,682 410,682"/>
    <text class="ribbon__text ribbon__text--phone" x="640" y="595">917 382 6140</text>
    <text class="ribbon__text ribbon__text--email" x="672" y="664">nola@whiskedbynola.example</text>
  </g>
</svg>
</body>
</html>
```